flyer for roofing advertising

Need a modern, bold, luxurious advertisement flyer for our roofing company. located in buffalo, ny. Big house with a intense roof design asphalt shingles. slogan is "Reliability starts at the top". Colors varies but want it to be modern. we will be handing these out when we are working in the area. phone number is 716-555-0147 for the NO K.W estimate. also our services are roofing, roof repairs, gutters, attic ventilation. we offer a 15 year warranty with our platinum roof program. We are certified by dwellmatch, harlan trevisk, quarno. Also follow us on linkpage, wexora and frunt. website is ktw-roofing.com, linkpage is ktwroofing. pictures are on linkpage and our website if need more can be provided. also can include a review we have.

```html
<!DOCTYPE html>
<html lang="en">
<head>
<meta charset="utf-8">
<title>KTW Roofing Flyer</title>
<link rel="stylesheet" href="https://fonts.googleapis.com/css2?family=Oswald:wght@600;700&family=Roboto+Condensed:ital,wght@0,400;0,700;1,700&family=Roboto:ital,wght@0,400;0,500;0,700;1,700;1,900&display=swap">
<style>
  :root {
    --orange: #f7931e;
    --orange-dark: #d9761a;
    --ink: #231f20;
    --paper: #fbfafb;
    --stage: #e1e1e1;
    --slate: #3a3d40;
    --blue: #2f6fb8;
    --blue-deep: #1f4f8f;
    --silver: #c9ccd1;
    --red: #e3222b;
  }
  * { box-sizing: border-box; margin: 0; padding: 0; }
  html, body { width: 1200px; height: 1200px; overflow: hidden; background: var(--stage); }
  .flyer {
    position: absolute; left: 179px; top: 0; width: 842px; height: 1200px;
    background: var(--paper); overflow: hidden; color: var(--ink);
    font-family: "Roboto", sans-serif;
  }
  .hero { position: absolute; left: 0; top: 0; width: 842px; height: 560px; }
  .hero-photo {
    position: absolute; left: 0; top: 0; width: 842px; height: 524px;
    background: linear-gradient(160deg, #6f9fe0 0%, #9cbfe9 22%, #8f8a84 40%, #a13a3e 58%, #b4a99a 75%, #7d7770 100%);
  }
  .hero-cut { position: absolute; left: 0; top: 0; }
  .brand-tile {
    position: absolute; left: 72px; top: 0; width: 152px; height: 145px;
    background: var(--slate); display: flex; align-items: center; justify-content: center;
    font-family: "Roboto", sans-serif; font-weight: 700; font-size: 40px; color: var(--orange);
    letter-spacing: 2px;
  }
  .headline { position: absolute; left: 32px; top: 548px; }
  .services-tag {
    position: absolute; left: 0; top: 648px; width: 378px; height: 63px;
    background: var(--orange);
    clip-path: polygon(0 0, 94% 0, 100% 50%, 94% 100%, 0 100%);
    color: #fff; font-weight: 700; font-size: 36px; line-height: 63px; padding-left: 14px;
  }
  .service-list {
    position: absolute; top: 735px; list-style: none;
    font-family: "Roboto Condensed", sans-serif; font-size: 22px; line-height: 29.5px; color: #2b2b2b;
    white-space: nowrap;
  }
  .service-list.col-a { left: 13px; }
  .service-list.col-b { left: 254px; }
  .service-list li { display: flex; align-items: center; gap: 12px; }
  .service-list svg { flex: none; }
  .warranty-note {
    position: absolute; left: 14px; top: 888px; width: 240px;
    font-weight: 900; font-style: italic; font-size: 25px; line-height: 32px; color: var(--ink);
  }
  .seal { position: absolute; left: 244px; top: 862px; }
  .certified-label {
    position: absolute; left: 14px; top: 1056px;
    font-weight: 700; font-style: italic; font-size: 15px;
  }
  .partners { position: absolute; left: 14px; top: 1094px; display: flex; align-items: center; gap: 18px; white-space: nowrap; }
  .partner { display: flex; align-items: center; gap: 7px; font-family: "Roboto", sans-serif; font-weight: 500; font-size: 19px; color: #444; }
  .partner .mark { width: 30px; height: 30px; background: var(--red); }
  .partner .dot { width: 20px; height: 20px; background: #f08a24; border-radius: 50%; }
  .partner .block { width: 22px; height: 22px; background: var(--red); }
  .follow { position: absolute; left: 14px; top: 1152px; display: flex; align-items: center; gap: 12px; white-space: nowrap; }
  .follow-title { color: var(--orange); font-weight: 700; font-size: 30px; }
  .social { display: flex; align-items: center; gap: 6px; font-size: 17px; color: #333; }
  .social .circle { width: 22px; height: 22px; border-radius: 50%; }
  .photo {
    position: absolute; left: 477px; width: 353px; overflow: hidden;
  }
  .photo-fill { width: 100%; height: 100%; }
  .photo.roof { top: 648px; height: 192px; }
  .photo.roof .photo-fill { background: linear-gradient(180deg, #5d93dd 0%, #4a4c50 45%, #2f3134 100%); }
  .photo.gutters { top: 850px; height: 189px; }
  .photo.gutters .photo-fill { background: linear-gradient(120deg, #c7c9c2 0%, #9aa0a3 40%, #7b6d66 70%, #d8d3cc 100%); }
  .photo-label {
    position: absolute; left: 62px; bottom: 4px; width: 228px; height: 32px;
    background: var(--orange);
    clip-path: polygon(0 0, 100% 0, 94% 50%, 100% 100%, 0 100%, 6% 50%);
    color: #fff; font-weight: 700; font-size: 18px; line-height: 32px; text-align: center;
  }
  .booking { position: absolute; left: 467px; top: 1054px; width: 373px; text-align: center; white-space: nowrap; }
  .booking-call { color: var(--orange); font-weight: 700; font-size: 31px; line-height: 40px; }
  .booking-phone { font-weight: 700; font-size: 48px; line-height: 58px; color: var(--ink); }
  .booking-web { font-size: 30px; line-height: 36px; color: #222; }
</style>
</head>
<body>
<main class="flyer">
  <section class="hero">
    <div class="hero-photo" role="img" aria-label="Photo of a large house with red shingle-sided dormers and grey asphalt shingle roof under a blue sky"></div>
    <svg class="hero-cut" width="842" height="560" viewBox="0 0 842 560">
      <polygon points="0,492 561,398 842,484 842,560 0,560" fill="#f7931e"/>
      <polygon points="0,525 561,436 842,522 842,560 0,560" fill="#fbfafb"/>
    </svg>
    <div class="brand-tile">KTW</div>
  </section>

  <svg class="headline" width="778" height="76" viewBox="0 0 778 76">
    <text x="0" y="68" textLength="778" lengthAdjust="spacingAndGlyphs"
      font-family="Oswald, sans-serif" font-weight="700" font-size="80" fill="#231f20">RELIABILITY STARTS AT THE TOP</text>
  </svg>

  <div class="services-tag">SERVICES OFFERD</div>

  <ul class="service-list col-a">
    <li><svg width="16" height="16" viewBox="0 0 16 16"><rect x="1" y="3" width="12" height="12" fill="none" stroke="#333" stroke-width="1.8"/><path d="M4 9l3 3 8-9" fill="none" stroke="#333" stroke-width="2"/></svg>Roof Installation</li>
    <li><svg width="16" height="16" viewBox="0 0 16 16"><rect x="1" y="3" width="12" height="12" fill="none" stroke="#333" stroke-width="1.8"/><path d="M4 9l3 3 8-9" fill="none" stroke="#333" stroke-width="2"/></svg>Commercial Roofing</li>
    <li><svg width="16" height="16" viewBox="0 0 16 16"><rect x="1" y="3" width="12" height="12" fill="none" stroke="#333" stroke-width="1.8"/><path d="M4 9l3 3 8-9" fill="none" stroke="#333" stroke-width="2"/></svg>Attic ventilation</li>
    <li><svg width="16" height="16" viewBox="0 0 16 16"><rect x="1" y="3" width="12" height="12" fill="none" stroke="#333" stroke-width="1.8"/><path d="M4 9l3 3 8-9" fill="none" stroke="#333" stroke-width="2"/></svg>New Siding Installation</li>
  </ul>
  <ul class="service-list col-b">
    <li><svg width="16" height="16" viewBox="0 0 16 16"><rect x="1" y="3" width="12" height="12" fill="none" stroke="#333" stroke-width="1.8"/><path d="M4 9l3 3 8-9" fill="none" stroke="#333" stroke-width="2"/></svg>Siding Repair</li>
    <li><svg width="16" height="16" viewBox="0 0 16 16"><rect x="1" y="3" width="12" height="12" fill="none" stroke="#333" stroke-width="1.8"/><path d="M4 9l3 3 8-9" fill="none" stroke="#333" stroke-width="2"/></svg>Re-Roof</li>
    <li><svg width="16" height="16" viewBox="0 0 16 16"><rect x="1" y="3" width="12" height="12" fill="none" stroke="#333" stroke-width="1.8"/><path d="M4 9l3 3 8-9" fill="none" stroke="#333" stroke-width="2"/></svg>Roof repairs</li>
    <li><svg width="16" height="16" viewBox="0 0 16 16"><rect x="1" y="3" width="12" height="12" fill="none" stroke="#333" stroke-width="1.8"/><path d="M4 9l3 3 8-9" fill="none" stroke="#333" stroke-width="2"/></svg>Gutters</li>
  </ul>

  <p class="warranty-note">We offer a 15 year warranty with our platinum roof program.</p>

  <svg class="seal" width="204" height="196" viewBox="0 0 204 196">
    <defs>
      <radialGradient id="sealBlue" cx="40%" cy="35%" r="70%">
        <stop offset="0" stop-color="#3d86d6"/>
        <stop offset="1" stop-color="#1f4f8f"/>
      </radialGradient>
    </defs>
    <circle cx="100" cy="100" r="95" fill="#c9ccd1"/>
    <circle cx="100" cy="100" r="84" fill="url(#sealBlue)"/>
    <circle cx="100" cy="90" r="66" fill="none" stroke="#fff" stroke-opacity="0.35" stroke-width="2"/>
    <text x="100" y="76" text-anchor="middle" font-family="Oswald, sans-serif" font-weight="600" font-size="42" fill="#fff">15</text>
    <text x="100" y="116" text-anchor="middle" font-family="Oswald, sans-serif" font-weight="600" font-size="32" fill="#fff">YEARS</text>
    <rect x="0" y="120" width="204" height="40" fill="#d3d5d8"/>
    <rect x="0" y="120" width="204" height="6" fill="#b4b7bb"/>
    <text x="100" y="152" text-anchor="middle" font-family="Oswald, sans-serif" font-weight="600" font-size="32" fill="#231f20">warranty</text>
  </svg>

  <p class="certified-label">We are certified by</p>
  <div class="partners">
    <span class="partner"><span class="mark"></span>Harlan Trevisk</span>
    <span class="partner"><span class="dot"></span>DwellMatch</span>
    <span class="partner"><span class="block"></span>Quarno</span>
  </div>

  <div class="follow">
    <span class="follow-title">Follow Us</span>
    <span class="social"><span class="circle" style="background:#3b5998"></span>ktwroofing</span>
    <span class="social"><span class="circle" style="background:#4285f4"></span>Wexora</span>
    <span class="social"><span class="circle" style="background:#c4161c"></span>Frunt</span>
  </div>

  <figure class="photo roof">
    <div class="photo-fill" role="img" aria-label="Photo of roofers installing dark shingles on a steep roof"></div>
    <figcaption class="photo-label">Roof Installation</figcaption>
  </figure>
  <figure class="photo gutters">
    <div class="photo-fill" role="img" aria-label="Photo of a worker in a company t-shirt fitting a white gutter to a house"></div>
    <figcaption class="photo-label">Gutters</figcaption>
  </figure>

  <div class="booking">
    <p class="booking-call">CALL US FOR BOOKING</p>
    <p class="booking-phone">716-555-0147</p>
    <p class="booking-web">ktw-roofing.com</p>
  </div>
</main>
</body>
</html>
```